International non-profit org needs web design

A new non-profit global organization called The Verdant Outreach Collective (VOC) needs a web design. The organization is a global community of professionals engaged in the commercialization aspects of innovation. The members of the community share experience and knowledge about exemplary practices and business models in order to continuoulsy improve the field of expertise.

Target Market(s)

governments, investors, universities, professionala

Industry/Entity Type

Non-Profit

Requirements
Must have
• landing page and capability to add tabs

```html
<!DOCTYPE html>
<html lang="en">
<head>
<meta charset="utf-8">
<title>The Verdant Outreach Collective</title>
<link rel="stylesheet" href="https://fonts.googleapis.com/css2?family=Arimo:wght@400;700&family=Marcellus+SC&display=swap">
<style>
:root{
  --red:#e31b23;
  --red-dark:#c8141b;
  --black:#000;
  --ink:#1a1a1a;
  --grey:#cfcfcf;
  --white:#fff;
  --orange-dark:#d98605;
  --gold:#f4a21c;
}
*{box-sizing:border-box;margin:0;padding:0}
html,body{width:978px;height:1200px;overflow:hidden;background:var(--white)}
body{font-family:"Arimo",Arial,sans-serif;color:var(--ink);position:relative}
.site-header{position:absolute;left:0;top:0;width:978px;height:113px;background:var(--white)}
.brand-name{position:absolute;left:22px;top:30px;width:290px;font-family:"Arimo",Arial,sans-serif;font-weight:700;font-size:22px;line-height:26px;color:var(--red)}
.main-nav{position:absolute;left:334px;top:8px;width:636px;height:96px;border-radius:12px;background:linear-gradient(#f04a50,var(--red) 40%,var(--red-dark));display:flex;padding:14px 10px 0}
.nav-item{flex:auto;text-align:center;color:var(--white);font-weight:700;font-size:13px;border-right:1px solid rgba(255,255,255,.35);height:68px;text-decoration:none}
.nav-item:last-child{border-right:0}
.nav-item svg{display:block;margin:2px auto 6px;width:32px;height:32px}
.hero{position:absolute;left:0;top:113px;width:978px;height:376px;background:var(--black)}
.hero-title{position:absolute;left:71px;top:32px;font-family:"Marcellus SC",serif;font-size:28px;letter-spacing:-1px;color:var(--white);font-weight:400}
.hero-text{position:absolute;left:75px;top:89px;width:412px;font-size:12.5px;line-height:21.5px;color:var(--white);letter-spacing:.2px}
.btn-read{position:absolute;left:361px;top:287px;width:116px;height:34px;border-radius:17px;background:linear-gradient(#f0474d,var(--red-dark));color:var(--white);font-weight:700;font-size:13px;line-height:34px;text-align:center;border:0}
.hero-photo{position:absolute;left:488px;top:0;width:490px;height:376px;background:radial-gradient(ellipse at 45% 35%,#c9a48f 0,#8d7a73 25%,#7f93b4 55%,#2a3344 100%)}
.hero-arrow{position:absolute;top:149px;width:38px;height:76px}
.hero-arrow.prev{left:0}
.hero-arrow.next{right:0}
.welcome{position:absolute;left:0;top:489px;width:978px;height:268px;background:var(--grey)}
.welcome h1{position:absolute;left:23px;top:20px;font-family:"Marcellus SC",serif;font-weight:400;font-size:28px;letter-spacing:-1px;color:var(--ink)}
.welcome h1 span{color:var(--red)}
.welcome-body{position:absolute;left:24px;top:90px;width:936px;font-size:12px;line-height:21.5px;color:var(--ink)}
.welcome-body p+p{margin-top:21.5px}
.features{position:absolute;left:0;top:757px;width:978px;height:334px;display:flex}
.panel{position:relative;height:334px}
.panel h2{height:44px;line-height:44px;font-size:13.5px;font-weight:700;border-bottom:1px solid rgba(255,255,255,.5);padding-left:23px}
.panel-objective{width:310px;background:radial-gradient(ellipse at 50% 55%,#4a4a4a,#262626);color:var(--white)}
.panel-objective h2{color:var(--gold)}
.objective-list{list-style:none;padding:6px 8px 0 33px}
.objective-list li{position:relative;font-size:12px;letter-spacing:-.1px;line-height:21.5px;margin-bottom:21.5px}
.objective-list li::before{content:"";position:absolute;left:-15px;top:6px;border-left:7px solid var(--white);border-top:5px solid transparent;border-bottom:5px solid transparent}
.panel-steps{width:335px;background:radial-gradient(ellipse at 50% 50%,#ee2a31,#c0121a);color:var(--white)}
.panel-steps h2{padding-left:9px}
.step{display:flex;align-items:center;gap:10px;margin:12px 0 0 14px;height:74px}
.step-badge{width:72px;height:72px;border-radius:50%;background:radial-gradient(circle at 50% 30%,#666,#000 60%);border:3px solid #e8e8e8;color:var(--white);font-weight:700;font-size:20px;display:flex;align-items:center;justify-content:center;flex:none}
.step p{font-size:12px;line-height:17.5px;width:195px}
.panel-news{width:333px;background:radial-gradient(ellipse at 50% 50%,#f7a11a,var(--orange-dark));color:var(--ink)}
.panel-news h2{padding-left:16px}
.news-item{margin:0 15px 0 24px;padding:16px 0 18px;border-bottom:1px solid rgba(120,70,0,.45)}
.news-item:last-child{border-bottom:0}
.news-item p{font-size:12px;line-height:17.5px;color:#3a2500}
.news-meta{display:flex;justify-content:space-between;margin-top:14px;font-weight:700;font-size:12.5px}
.site-footer{position:absolute;left:0;top:1091px;width:978px;height:109px;background:var(--grey)}
.footer-band{position:absolute;left:0;top:19px;width:978px;height:90px;background:var(--black);border-top:3px solid var(--red)}
.footer-nav{text-align:center;margin-top:23px;font-size:13px;color:var(--white)}
.footer-nav a{color:var(--white);text-decoration:none;padding:0 10px}
.footer-nav span{color:var(--white)}
.copyright{text-align:center;font-size:12.5px;color:var(--white);margin-top:10px}
</style>
</head>
<body>
<header class="site-header">
  <div class="brand-name">The Verdant Outreach Collective</div>
  <nav class="main-nav">
    <a class="nav-item" href="#"><svg viewBox="0 0 32 32" fill="none" stroke="#fff" stroke-width="2.5"><circle cx="16" cy="16" r="13"/><ellipse cx="16" cy="16" rx="6" ry="13"/><path d="M3 16h26M5 9h22M5 23h22"/></svg>Home</a>
    <a class="nav-item" href="#"><svg viewBox="0 0 32 32" fill="#fff"><circle cx="11" cy="9" r="5"/><circle cx="22" cy="9" r="5"/><path d="M1 30c0-9 4-13 10-13s10 4 10 13zM13 30c0-9 4-13 9-13s9 4 9 13z"/></svg>About Us</a>
    <a class="nav-item" href="#"><svg viewBox="0 0 32 32" fill="#fff"><circle cx="11" cy="20" r="8"/><circle cx="23" cy="9" r="7"/><circle cx="11" cy="20" r="3" fill="#e31b23"/><circle cx="23" cy="9" r="2.5" fill="#e31b23"/></svg>Services</a>
    <a class="nav-item" href="#"><svg viewBox="0 0 32 32" fill="none" stroke="#fff" stroke-width="2.5"><path d="M16 3a9 9 0 0 0-5 16v4h10v-4a9 9 0 0 0-5-16z"/><path d="M12 27h8M13 30h6"/></svg>Ideas</a>
    <a class="nav-item" href="#"><svg viewBox="0 0 32 32" fill="#fff"><rect x="5" y="14" width="20" height="16" rx="2"/><path d="M20 14V9a5 5 0 0 1 10 0v3" fill="none" stroke="#fff" stroke-width="3"/></svg>What we do?</a>
    <a class="nav-item" href="#"><svg viewBox="0 0 32 32" fill="#fff"><rect x="2" y="9" width="28" height="20" rx="2"/><path d="M11 9V5h10v4" fill="none" stroke="#fff" stroke-width="2.5"/><rect x="2" y="16" width="28" height="2" fill="#e31b23"/></svg>Contact Us</a>
  </nav>
</header>

<section class="hero">
  <h2 class="hero-title">Lorem Ipsum is Simply</h2>
  <p class="hero-text">Lorem Ipsum is simply dummy text of the printing and typesetting industry. Lorem Ipsum has been the industry's standard dummy text ever since the 1500s, when an unknown printer took a galley of type and scrambled it to make a type specimen book. It has survived not only five centuries, but also the leap into electronic typesetting, remaining essentially unchanged. It was popularised in the 1960s with the release of Typeleaf sheets containing Lorem Ipsum passages, and more recently with desktop publishing software like Quillset Composer including versions of Lorem Ipsum.</p>
  <button class="btn-read">Read More</button>
  <div class="hero-photo" role="img" aria-label="Photo of a smiling professional woman in a light blue shirt seated in an office chair"></div>
  <svg class="hero-arrow prev" viewBox="0 0 38 76"><path d="M0 0a38 38 0 0 1 0 76z" fill="#e31b23"/><path d="M19 28v20l-11-10z" fill="#fff"/></svg>
  <svg class="hero-arrow next" viewBox="0 0 38 76"><path d="M38 0a38 38 0 0 0 0 76z" fill="#e31b23"/><path d="M19 28v20l11-10z" fill="#fff"/></svg>
</section>

<section class="welcome">
  <h1>Welcome to <span>Our Website</span></h1>
  <div class="welcome-body">
    <p>Lorem Ipsum is simply dummy text of the printing and typesetting industry. Lorem Ipsum has been the industry's standard dummy text ever since the 1500s, when an unknown printer took a galley of type and scrambled it to make a type specimen book. It has survived not only five centuries, but also the leap into electronic typesetting, remaining essentially unchanged. It was popularised in the 1960s with the release of Typeleaf sheets containing Lorem Ipsum passages, and more recently with desktop publishing software like Quillset Composer including versions of Lorem Ipsum.</p>
    <p>Lorem Ipsum is simply dummy text of the printing and typesetting industry. Lorem Ipsum has been the industry's standard dummy text ever since the 1500s, when an unknown printer took a galley of type and scrambled it to make</p>
  </div>
</section>

<section class="features">
  <div class="panel panel-objective">
    <h2>The Objective</h2>
    <ul class="objective-list">
      <li>Lorem Ipsum is simply dummy text of the printing and typesetting industry.</li>
      <li>Lorem Ipsum is simply dummy text of the printing and typesetting industry.</li>
      <li>Lorem Ipsum is simply dummy text of the printing and typesetting industry.</li>
      <li>Lorem Ipsum is simply dummy text of the printing and typesetting industry.</li>
    </ul>
  </div>
  <div class="panel panel-steps">
    <h2>How it Works</h2>
    <div class="step"><div class="step-badge">01</div><p>Lorem Ipsum is simply dummy text of the printing and typesetting industry.</p></div>
    <div class="step"><div class="step-badge">02</div><p>Lorem Ipsum is simply dummy text of the printing and typesetting industry.</p></div>
    <div class="step"><div class="step-badge">03</div><p>Lorem Ipsum is simply dummy text of the printing and typesetting industry.</p></div>
  </div>
  <div class="panel panel-news">
    <h2>Latest News</h2>
    <article class="news-item">
      <p>Lorem Ipsum is simply dummy text of the printing and typesetting industry Lorem Ipsum is simply dummy text of the printing and typesetting industry.</p>
      <div class="news-meta"><span>Jan/10/2011</span><span>James, UK</span></div>
    </article>
    <article class="news-item">
      <p>Lorem Ipsum is simply dummy text of the printing and typesetting industry Lorem Ipsum is simply dummy text of the printing and typesetting industry.dummy text of the printing and typesetting industry.</p>
      <div class="news-meta"><span>Jan/10/2011</span><span>James, UK</span></div>
    </article>
  </div>
</section>

<footer class="site-footer">
  <div class="footer-band">
    <nav class="footer-nav">
      <a href="#">Home</a><span>|</span><a href="#">About Us</a><span>|</span><a href="#">Services</a><span>|</span><a href="#">Ideas</a><span>|</span><a href="#">What we do?</a><span>|</span><a href="#">Contact Us</a>
    </nav>
    <p class="copyright">Copyright © 2011 VOC</p>
  </div>
</footer>
</body>
</html>
```